One-page magazine ad for accountant serving the non-profit industry

I am Certified Public Accountant placing a one-page ad in Harvestlight Journal. The ad will be seen by churches and other non-profit organizations.
Harvestlight Journal requires the following:
Accepted file formats:
a) Press ready PDF with all fonts embedded. OR
b) Flattened CMYK Abode Photoshop PSD or illustrator PDF or EPS with all fonts outlined.
Ad Specs:
Trim 8" x 10.5"
Live 7.5" x 10"
Bleed 8.25" x 10.75"

I would like the ad to state the following information:

Marcus T. Velloway, CPA, CGMA

I am Certified Public Accountant with over 30 years of experience serving the accounting and tax needs of churches and non-profit organizations.

Some of the services I can offer:

Audits, Reviews, Compilations
Bookkeeping Services
Payroll Taxes
501C3 - IRS exemption applications
Clergy Housing Allowance issues and Personal Taxes

```html
<!DOCTYPE html>
<html lang="en">
<head>
<meta charset="utf-8">
<title>Marcus T. Velloway, CPA, CGMA – Harvestlight Journal Ad</title>
<link rel="stylesheet" href="https://fonts.googleapis.com/css2?family=Source+Sans+3:wght@300;400;600;700;800&display=swap">
<style>
  :root {
    --sky-light: #f4f6f8;
    --sky-mid: #cfd8df;
    --sky-deep: #b4c2cd;
    --teal-band: #0e5b79;
    --teal-band-dark: #0a4d68;
    --offer-blue: #1b8fcf;
    --offer-blue-dark: #0d6aa8;
    --offer-fold: #0a4f80;
    --slate: #b7c2ca;
    --slate-light: #c8d1d7;
    --accent-gold: #f5b400;
    --ink: #111111;
    --ink-soft: #545b61;
    --name-blue: #1a6b91;
    --headline: #3b3f42;
    --white: #ffffff;
  }
  html, body {
    margin: 0;
    padding: 0;
    overflow: hidden;
    background: #e9edf0;
  }
  .ad {
    position: relative;
    width: 914px;
    height: 1200px;
    overflow: hidden;
    font-family: "Source Sans 3", "Helvetica Neue", Arial, sans-serif;
    background: var(--white);
  }
  .hero {
    position: absolute;
    left: 0; top: 0;
    width: 914px; height: 594px;
    background: radial-gradient(ellipse at 45% 30%, var(--sky-light) 0%, var(--sky-mid) 60%, var(--sky-deep) 100%);
  }
  .hero-plant {
    position: absolute;
    left: 40px; top: 10px;
    width: 330px; height: 632px;
    background: linear-gradient(180deg, #6aa13a 0%, #4f8a2a 55%, #c9c7c4 80%, #b9b6b2 100%);
    border-radius: 40px 40px 6px 6px;
    opacity: .85;
  }
  .hero-watering {
    position: absolute;
    left: 385px; top: 0;
    width: 529px; height: 390px;
    background: linear-gradient(200deg, #3a3d42 0%, #c9b6a6 30%, #a9adb0 60%, rgba(169,173,176,0) 100%);
    border-radius: 0 0 0 180px;
    opacity: .8;
  }
  .headline {
    position: absolute;
    left: 366px; top: 404px;
    margin: 0;
    font-weight: 300;
    font-size: 49px;
    line-height: 55px;
    color: var(--headline);
    letter-spacing: -0.5px;
  }
  .side-growth {
    position: absolute;
    left: 0; top: 594px;
    width: 210px; height: 256px;
    background: linear-gradient(160deg, #0c2f3f 0%, #2a6f86 45%, #8fc1cc 75%, #3b7f8f 100%);
  }
  .side-chart {
    position: absolute;
    left: 0; top: 850px;
    width: 210px; height: 350px;
    background: linear-gradient(180deg, #ffffff 0%, #f1f3f5 40%, #c9ced3 100%);
  }
  .services {
    position: absolute;
    left: 210px; top: 594px;
    width: 704px; height: 352px;
    background: linear-gradient(180deg, var(--teal-band) 0%, var(--teal-band-dark) 100%);
  }
  .services-title {
    position: absolute;
    left: 120px; top: 20px;
    margin: 0;
    color: var(--white);
    font-weight: 700;
    font-size: 30px;
    letter-spacing: -0.2px;
  }
  .services-list {
    position: absolute;
    left: 158px; top: 58px;
    margin: 0; padding: 0;
    list-style: none;
  }
  .services-list li {
    position: relative;
    padding-left: 17px;
    height: 32px;
    line-height: 20px;
    color: var(--white);
    font-weight: 700;
    font-size: 17px;
  }
  .services-list li::before {
    content: "";
    position: absolute;
    left: 0; top: 5px;
    width: 11px; height: 11px;
    background: var(--accent-gold);
  }
  .footer-band {
    position: absolute;
    left: 210px; top: 946px;
    width: 704px; height: 254px;
    background: linear-gradient(180deg, var(--slate) 0%, var(--slate-light) 100%);
  }
  .offer {
    position: absolute;
    top: 822px;
    width: 305px; height: 150px;
  }
  .offer svg { position: absolute; left: 0; top: 0; }
  .offer-text {
    position: absolute;
    left: 20px; right: 20px; top: 16px;
    margin: 0;
    text-align: center;
    color: var(--white);
    font-size: 20px;
    line-height: 25px;
  }
  .offer-text strong {
    font-weight: 400;
    font-size: 30px;
    line-height: 30px;
  }
  .offer-ebook { left: 231px; }
  .offer-review { left: 557px; }
  .offer-review .offer-text { top: 14px; }
  .bio-name {
    position: absolute;
    left: 268px; top: 986px;
    margin: 0;
    color: var(--name-blue);
    font-weight: 700;
    font-size: 22px;
  }
  .bio-text {
    position: absolute;
    left: 268px; top: 1020px;
    width: 600px;
    margin: 0;
    color: var(--ink-soft);
    font-weight: 700;
    font-size: 15.5px;
    line-height: 21px;
  }
  .contact {
    position: absolute;
    left: 514px; top: 1108px;
    margin: 0;
    font-style: normal;
    color: var(--ink);
    font-weight: 700;
    font-size: 17.5px;
    line-height: 22px;
  }
  .accent-bar {
    position: absolute;
    left: 513px; top: 1172px;
    width: 401px; height: 28px;
    background: var(--accent-gold);
  }
</style>
</head>
<body>
<main class="ad">
  <section class="hero">
    <div class="hero-plant" role="img" aria-label="Potted leafy plant growing in the shape of a dollar sign"></div>
    <div class="hero-watering" role="img" aria-label="Hand in a business suit sleeve holding a metal watering can"></div>
    <h1 class="headline">Certified Public<br>Accountant<br>at your Reach</h1>
  </section>

  <div class="side-growth" role="img" aria-label="Teal digital bar graph with rising arrows"></div>
  <div class="side-chart" role="img" aria-label="White 3D bar chart with a dark arrow curving upward"></div>

  <section class="services">
    <h2 class="services-title">Some of the services I can offer:</h2>
    <ul class="services-list">
      <li>Audits, Reviews, Compilations</li>
      <li>Bookkeeping Services</li>
      <li>Payroll Taxes</li>
      <li>501C3 - IRS exemption applications</li>
      <li>Clergy Housing Allowance issues and Personal Taxes</li>
    </ul>
  </section>

  <div class="footer-band"></div>

  <aside class="offer offer-ebook">
    <svg width="305" height="150" viewBox="0 0 305 150" aria-hidden="true">
      <defs>
        <linearGradient id="offerFillA" x1="0" y1="0" x2="0" y2="1">
          <stop offset="0" stop-color="#2aa0dc"/>
          <stop offset="1" stop-color="#0d6aa8"/>
        </linearGradient>
      </defs>
      <polygon points="0,132 14,150 14,132" fill="#0a4f80"/>
      <polygon points="14,0 305,0 305,132 291,150 0,132 0,14" fill="url(#offerFillA)"/>
      <polygon points="0,14 14,0 14,14" fill="#0a4f80"/>
    </svg>
    <p class="offer-text">E-mail us to request our<br><strong>FREE</strong> informational<br>eBook on the 7 biggest<br>mistakes churches make.</p>
  </aside>

  <aside class="offer offer-review">
    <svg width="305" height="150" viewBox="0 0 305 150" aria-hidden="true">
      <defs>
        <linearGradient id="offerFillB" x1="0" y1="0" x2="0" y2="1">
          <stop offset="0" stop-color="#2aa0dc"/>
          <stop offset="1" stop-color="#0d6aa8"/>
        </linearGradient>
      </defs>
      <polygon points="0,0 291,0 305,14 305,150 14,150 0,132" fill="url(#offerFillB)"/>
      <polygon points="291,0 305,14 291,14" fill="#0a4f80"/>
    </svg>
    <p class="offer-text">PLUS,<br>get a <strong>FREE review</strong><br>of your church’s accounting<br>processes.</p>
  </aside>

  <h3 class="bio-name">Marcus T. Velloway, CPA, CGMA</h3>
  <p class="bio-text">Certified Public Accountant with over 30 years of experience serving the accounting and tax needs of churches and non-profit organizations.</p>

  <address class="contact">
    Marcus T. Velloway, CPA, CGMA<br>
    Email: marcus@vellowaycpa.com<br>
    Telephone: (555) 214-3906
  </address>

  <div class="accent-bar"></div>
</main>
</body>
</html>
```